Marcus Lindqvist Photography needs a business card designs

I am looking for a business card with a logo clean and simple which I can use that logo on my website or on my pictures. It has to be very classy and very professional. Please look at my website at www.marcuslvqphoto.com for my signature. I'm thinking of something like that for my signature/logo. I'm still working on my website but you get an idea. I'm open to any design but not too busy graphics.

I will be printing the business card from qrivel.com.

Surprise me :)

contact me if you have any questions.

-ML

I'm receiving a lot of black background at the moment. I know my website is all black doesn't mean I want my card to be all black. Please send in with some white background as well. Thanks :)

check out some business cards that I found online. I think they are simple and look really awesome. I don't want a card that is too busy.

http://www.marcuslvqphoto.com/p270092084

Reason: Please extend the date for me. I haven't really receive any good design yet.

Printing

• -a logo that related to my first and last initial of my name "ML"
-double sided
• -I don't want my background to be all black.
-no pictures on the card

```html
<!DOCTYPE html>
<html lang="en">
<head>
<meta charset="utf-8">
<title>Marcus Lindqvist Photography – Business Card</title>
<link rel="stylesheet" href="https://fonts.googleapis.com/css2?family=Jost:wght@500&family=Roboto+Condensed:wght@400;700&display=swap">
<style>
  :root {
    --paper: #ffffff;
    --card-red: #8b111a;
    --ink-dark: #2a0a0c;
    --ink-light: #ffffff;
    --shadow: rgba(0, 0, 0, 0.45);
  }
  html, body {
    margin: 0;
    padding: 0;
    overflow: hidden;
    background: var(--paper);
  }
  .canvas {
    position: relative;
    width: 1200px;
    height: 900px;
    background: var(--paper);
    overflow: hidden;
  }
  .card {
    position: absolute;
    width: 500px;
    height: 286px;
    background: var(--card-red);
    box-shadow: 3px 4px 5px var(--shadow);
    overflow: hidden;
  }
  .card--front { left: 124px; top: 114px; }
  .card--back  { left: 576px; top: 500px; }

  .monogram {
    position: absolute;
    left: 0;
    top: 0;
    width: 100%;
    height: 100%;
    display: flex;
    align-items: center;
    justify-content: center;
    gap: 18px;
    font-family: "Jost", sans-serif;
    font-weight: 500;
    font-size: 150px;
    line-height: 1;
    letter-spacing: 4px;
    color: var(--ink-dark);
  }
  .monogram__mark {
    width: 22px;
    height: 22px;
    background: var(--ink-dark);
  }

  .back__content {
    position: absolute;
    inset: 0;
    text-align: center;
    color: var(--ink-light);
  }
  .brand-name {
    position: absolute;
    left: 0;
    right: 0;
    top: 30px;
    font-family: "Jost", sans-serif;
    font-weight: 500;
    font-size: 38px;
    line-height: 1;
    color: var(--ink-light);
  }
  .brand-tag {
    position: absolute;
    left: 0;
    right: 0;
    top: 80px;
    font-family: "Jost", sans-serif;
    font-weight: 500;
    font-size: 33px;
    line-height: 1;
    letter-spacing: 0.5px;
    color: var(--ink-dark);
  }
  .contact-phone {
    position: absolute;
    left: 0;
    right: 0;
    top: 124px;
    font-family: "Roboto Condensed", sans-serif;
    font-weight: 700;
    font-size: 50px;
    line-height: 1;
    letter-spacing: 1px;
  }
  .contact-email,
  .contact-web {
    position: absolute;
    left: 0;
    right: 0;
    font-family: "Roboto Condensed", sans-serif;
    font-weight: 400;
    font-size: 27px;
    line-height: 1;
  }
  .contact-email { top: 194px; font-size: 25px; }
  .contact-web   { top: 234px; }
</style>
</head>
<body>
  <main class="canvas">
    <section class="card card--front" aria-label="Card front">
      <div class="monogram">
        <span class="monogram__mark" aria-hidden="true"></span>
        <span class="monogram__letters">ML</span>
      </div>
    </section>

    <section class="card card--back" aria-label="Card back">
      <div class="back__content">
        <div class="brand-name">Marcus Lindqvist</div>
        <div class="brand-tag">PHOTOGRAPHY</div>
        <div class="contact-phone">0198 765 432</div>
        <div class="contact-email">marcus@marcuslvqphotography.com</div>
        <div class="contact-web">www.marcuslvqphoto.com</div>
      </div>
    </section>
  </main>
</body>
</html>
```